Law Firm Needs Brochure Redesign Using New Logo

We are a personal injury law firm that does auto injuries and other personal injury cases. We want a new brochure that has our updated logo and information. Instead of gold and black, we want more navy, as matches the new logo. The Auto Liability portion should read: "(required by the state of Arizona in the amounts of $25,000 per person / $50,000 per accident, but a higher amount may be best )." The other information can remain the same. We'd like the brochure to keep the same professional tone as the previous brochure.
Our website is https://www.marbrenlegal.com/.

```html
<!DOCTYPE html>
<html lang="en">
<head>
<meta charset="utf-8">
<title>Marbren Law – Car Accident Brochure</title>
<link rel="stylesheet" href="https://fonts.googleapis.com/css2?family=Hind:wght@500;600&family=Inter:wght@400&family=Quicksand:wght@700&display=swap">
<style>
  :root{
    --ink:#171717;
    --navy:#0a2244;
    --navy-deep:#0d2347;
    --steel:#33639a;
    --frame:#2e5a8e;
    --highlight:#1b3278;
    --muted:#5b86a0;
    --white:#ffffff;
    --photo-street-a:#76768e;
    --photo-street-b:#56586a;
    --photo-car-a:#9a9aac;
    --photo-car-b:#6c6c7c;
  }
  *{margin:0;padding:0;box-sizing:border-box}
  html,body{width:1200px;height:848px;overflow:hidden;background:var(--ink)}
  .brochure{position:relative;width:1200px;height:848px;overflow:hidden;background:var(--ink);font-family:"Inter",sans-serif;color:var(--white)}
  .photo{position:absolute;top:0;height:848px}
  .photo--street{left:84px;width:716px;background:linear-gradient(180deg,var(--photo-street-a) 0%,#6a6a7c 45%,var(--photo-street-b) 100%)}
  .photo--car{left:751px;width:449px;background:radial-gradient(circle at 75% 45%,#4a4a58 0%,transparent 28%),linear-gradient(160deg,var(--photo-car-a) 0%,var(--photo-car-b) 100%)}
  .shapes{position:absolute;inset:0;width:1200px;height:848px}

  .stats-panel{position:absolute;left:34px;top:21px;width:333px;height:756px;background:var(--navy);border:2px solid var(--frame)}
  .stat{position:absolute;left:0;width:100%;text-align:center}
  .stat__icon{width:70px;height:70px;border-radius:50%;background:#eef5fb;margin:0 auto;display:flex;align-items:center;justify-content:center}
  .stat__figure{font-family:"Quicksand",sans-serif;font-weight:700;font-size:34px;line-height:1;margin-top:26px}
  .stat__caption{font-size:15px;line-height:20px;color:var(--muted);margin-top:12px}
  .stat--crashes{top:70px}
  .stat--fatal{top:328px}
  .stats-panel__promise{position:absolute;left:22px;right:22px;top:602px;text-align:center;font-size:14.5px;line-height:17.2px}

  .practice{position:absolute;left:445px;width:280px;top:264px;text-align:center;font-size:14px;line-height:17.2px}

  .firm-mark{position:absolute;display:flex;align-items:center;gap:10px;font-family:"Hind",sans-serif;font-weight:600;letter-spacing:.5px}
  .firm-mark__dot{border-radius:50%}
  .firm-mark--contact{left:424px;top:645px;font-size:24px;color:var(--white)}
  .firm-mark--contact .firm-mark__dot{width:38px;height:38px;background:var(--white)}
  .firm-mark--cover{left:962px;top:762px;font-size:26px;color:var(--navy-deep)}
  .firm-mark--cover .firm-mark__dot{width:44px;height:44px;background:var(--navy-deep)}

  .contact{position:absolute;left:421px;top:706px;list-style:none;font-size:15px;line-height:20px}
  .contact li{display:flex;align-items:flex-start;gap:9px;position:absolute;left:0;white-space:nowrap}
  .contact svg{width:14px;height:14px;flex:none;margin-top:3px;fill:var(--white)}
  .contact__address{top:0}
  .contact__phone{top:52px}
  .contact__email{top:85px;color:var(--muted)}
  .contact__web{top:111px;color:var(--muted)}
  .contact a{color:inherit;text-decoration:none}

  .cover{position:absolute;left:830px;top:108px}
  .cover__title{font-family:"Hind",sans-serif;font-weight:600;font-size:62px;line-height:63px;letter-spacing:-.5px}
  .cover__title span{display:block}
  .cover__title .cover__accent{position:relative;margin-left:-7px;padding-left:7px;width:353px;background:var(--highlight);height:62px}
  .cover__lede{font-size:20px;line-height:26px;margin-top:14px;width:345px;color:#f2f2f6}
</style>
</head>
<body>
<main class="brochure">
  <div class="photo photo--street" role="img" aria-label="Blurred photo of a roadside street with trees"></div>
  <div class="photo photo--car" role="img" aria-label="Photo of a damaged silver car front and headlight"></div>

  <svg class="shapes" viewBox="0 0 1200 848" aria-hidden="true">
    <polygon points="368,392 800,848 368,848" fill="var(--ink)"/>
    <rect x="84" y="392" width="284" height="456" fill="var(--ink)"/>
    <polygon points="580,0 751,0 751,140" fill="var(--white)"/>
    <polygon points="1200,455 1200,848 790,848" fill="var(--white)"/>
    <polygon points="368,303 620,548 620,585 368,340" fill="var(--steel)"/>
    <polygon points="465,439 828,800 828,835 465,479" fill="var(--navy-deep)"/>
    <polygon points="904,700 1200,412 1200,460 904,730" fill="var(--steel)"/>
    <polygon points="1054,609 1200,470 1200,520 1054,644" fill="var(--navy-deep)"/>
    <polygon points="806,73 885,0 920,0 806,105" fill="var(--steel)"/>
    <polygon points="849,52 905,0 935,0 849,85" fill="var(--navy-deep)"/>
  </svg>

  <section class="stats-panel">
    <div class="stat stat--crashes">
      <div class="stat__icon">
        <svg width="40" height="30" viewBox="0 0 40 30" aria-hidden="true">
          <rect x="2" y="9" width="14" height="12" rx="3" fill="#e86a3a"/>
          <rect x="8" y="6" width="28" height="16" rx="4" fill="#3bb98a"/>
          <rect x="13" y="8" width="18" height="6" rx="2" fill="#bff0e0"/>
          <rect x="10" y="21" width="5" height="6" rx="1" fill="#2d4a5a"/>
          <rect x="29" y="21" width="5" height="6" rx="1" fill="#2d4a5a"/>
          <polygon points="33,2 37,5 35,8 39,9 34,11" fill="#f5a623"/>
        </svg>
      </div>
      <p class="stat__figure">107,000+</p>
      <p class="stat__caption">crashes will happen in the state<br>of Arizona this year.</p>
    </div>
    <div class="stat stat--fatal">
      <div class="stat__icon">
        <svg width="28" height="30" viewBox="0 0 28 30" aria-hidden="true">
          <rect x="7" y="8" width="14" height="16" rx="4" fill="#e84a5a"/>
          <rect x="3" y="23" width="22" height="5" rx="1" fill="#3b4250"/>
          <rect x="13" y="12" width="2" height="6" fill="#fff"/>
          <rect x="13" y="19" width="2" height="2" fill="#fff"/>
          <line x1="3" y1="3" x2="6" y2="6" stroke="#e84a5a" stroke-width="1.5"/>
          <line x1="25" y1="3" x2="22" y2="6" stroke="#e84a5a" stroke-width="1.5"/>
        </svg>
      </div>
      <p class="stat__figure">700+</p>
      <p class="stat__caption">among them will result in<br>fatalities.</p>
    </div>
    <p class="stats-panel__promise">If we don't win, you don't pay attorney fees. That seems fair to us. Know what's happening with your case, get the answers to your questions and work on getting better with the confidence that you've got an excellent group of people working for you.</p>
  </section>

  <p class="practice">Our primary practice is helping injury victims and their families through the process of insurance claims and litigation related to car accidents, trucking accidents, wrongful death and other serious injuries.</p>

  <div class="firm-mark firm-mark--contact"><span class="firm-mark__dot"></span>MARBREN LAW</div>

  <ul class="contact">
    <li class="contact__address"><svg viewBox="0 0 14 14"><path d="M7 0a5 5 0 0 0-5 5c0 3.6 5 9 5 9s5-5.4 5-9a5 5 0 0 0-5-5zm0 7a2 2 0 1 1 0-4 2 2 0 0 1 0 4z"/></svg><span>4810 N. Cedar Ridge Road Suite B140<br>Phoenix AZ 85018</span></li>
    <li class="contact__phone"><svg viewBox="0 0 14 14"><path d="M3 0l2.5 3-1.3 1.8a8 8 0 0 0 5 5L11 8.5 14 11l-1.8 2.5C6 13.5.5 8 .5 1.8z"/></svg><span>602.555.0142</span></li>
    <li class="contact__email"><svg viewBox="0 0 14 14"><path d="M0 3h14v1L7 8 0 4zM0 5.5l7 4 7-4V12H0z"/></svg><a href="mailto:info@marbrenlegal.com">info@marbrenlegal.com</a></li>
    <li class="contact__web"><svg viewBox="0 0 14 14"><path d="M7 0a7 7 0 1 0 0 14A7 7 0 0 0 7 0zm0 1.3c.9 1 1.5 2.4 1.7 4.2H5.3C5.5 3.7 6.1 2.3 7 1.3zM1.4 6.5h2.7c.1 1.6.5 3 1.1 4.1A5.7 5.7 0 0 1 1.4 6.5zm3.9 0h3.4c-.1 1.8-.8 3.3-1.7 4.3-.9-1-1.6-2.5-1.7-4.3zm4.6 0h2.7a5.7 5.7 0 0 1-3.8 4.1c.6-1.1 1-2.5 1.1-4.1z"/></svg><a href="https://www.marbrenlegal.com/">www.marbrenlegal.com</a></li>
  </ul>

  <section class="cover">
    <h1 class="cover__title">
      <span>Protect</span>
      <span>your family</span>
      <span>in case of a</span>
      <span class="cover__accent">car accident</span>
    </h1>
    <p class="cover__lede">A little knowledge and preparation go a long way</p>
  </section>

  <div class="firm-mark firm-mark--cover"><span class="firm-mark__dot"></span>MARBREN LAW</div>
</main>
</body>
</html>
```